Webdesign für Honigmanufaktur
Zielgruppe
Imkerei, Verkauf von Honig und Honigerzeugnissen, so wie Bienenwachskerzen.
Zielgruppe sind vermutlich Frauen im mittleren bis gehobenen Alter.
Aufgabenstellung
Es gibt ein Firmenlogo.
Ich bevorzuge als Grundfarbe weiß, lasse mich aber von guten Einfällen gerne überraschen.
Die Website www.velunda.at finde ich sehr ansprechend.
Nur ohne Musik.
Ohne Deutsch/Englisch Auswahl.
Es soll danach Word press verwendet werden.

```html
<!DOCTYPE html>
<html lang="de">
<head>
<meta charset="utf-8">
<title>Honigwerkstatt Lindenhain – Mobile Startseite</title>
<link href="https://fonts.googleapis.com/css2?family=Raleway:wght@400;800&family=Oswald:wght@500&display=swap" rel="stylesheet">
<style>
  :root {
    --page-bg: #f4f4f4;
    --screen-bg: #ffffff;
    --brown: #4a2408;
    --honey: #f2a532;
    --honey-deep: #e08a12;
    --honey-light: #f8d35a;
    --text-grey: #8a8a8a;
  }
  * { margin: 0; padding: 0; box-sizing: border-box; }
  html, body {
    width: 1062px; height: 1200px; overflow: hidden;
    background: var(--page-bg);
  }
  .mobile-page {
    position: absolute; left: 261px; top: 122px;
    width: 540px; height: 956px;
    background: var(--screen-bg);
    overflow: hidden;
  }
  .brand {
    position: absolute; left: 38px; top: 138px;
    display: flex; align-items: center; gap: 10px;
  }
  .brand-square {
    width: 22px; height: 22px; background: var(--brown);
  }
  .brand-name {
    font-family: "Oswald", sans-serif; font-weight: 500;
    font-size: 20px; line-height: 1.15; letter-spacing: 0.5px;
    color: var(--brown); text-transform: uppercase;
  }
  .menu-toggle {
    position: absolute; left: 438px; top: 60px;
    width: 70px; height: 44px;
    display: flex; flex-direction: column; justify-content: space-between;
  }
  .menu-toggle span {
    display: block; height: 7px; background: var(--brown);
  }
  .honey-visual {
    position: absolute; left: 296px; top: 140px;
    width: 244px; height: 250px;
    background: radial-gradient(closest-side at 55% 50%, var(--honey-light) 0%, var(--honey) 45%, rgba(242,165,50,0.35) 75%, rgba(242,165,50,0) 100%);
  }
  .bee-collage {
    position: absolute; left: 0; top: 301px;
    width: 540px; height: 402px;
  }
  .headline {
    position: absolute; left: 46px; top: 778px;
    font-family: "Raleway", sans-serif; font-weight: 800;
    font-size: 40px; line-height: 50px; text-transform: uppercase;
  }
  .headline .line-main { color: var(--brown); display: block; }
  .headline .line-sub { color: var(--honey); display: block; }
  .intro {
    position: absolute; left: 46px; top: 920px;
    font-family: "Raleway", sans-serif; font-weight: 400;
    font-size: 23px; color: var(--text-grey); white-space: nowrap;
  }
</style>
</head>
<body>
  <main class="mobile-page">
    <div class="menu-toggle" aria-label="Menü"><span></span><span></span><span></span></div>

    <div class="brand">
      <div class="brand-square"></div>
      <div class="brand-name">Honigwerkstatt<br>Lindenhain</div>
    </div>

    <div class="honey-visual" role="img" aria-label="Honiglöffel, von dem Honig tropft"></div>

    <svg class="bee-collage" viewBox="0 0 540 402" role="img" aria-label="Biene auf einer gelben Blüte in Wabenform">
      <defs>
        <radialGradient id="bloom" cx="0.42" cy="0.62" r="0.7">
          <stop offset="0" stop-color="#b8650e"/>
          <stop offset="0.35" stop-color="#e6a625"/>
          <stop offset="1" stop-color="#f6d65e"/>
        </radialGradient>
        <clipPath id="combs">
          <polygon points="2,132 76,5 222,5 296,132 222,259 76,259"/>
          <polygon points="223,259 296,132 443,132 517,259 443,386 296,386"/>
          <polygon points="2,386 76,259 222,259 296,386 222,513 76,513"/>
          <polygon points="444,132 517,5 664,5 738,132 664,259 517,259"/>
          <polygon points="444,386 517,259 664,259 738,386 664,513 517,513"/>
        </clipPath>
      </defs>
      <rect width="540" height="402" fill="url(#bloom)" clip-path="url(#combs)"/>
      <g stroke="#ffffff" stroke-width="2" fill="none">
        <polyline points="76,259 222,259 296,386 296,402"/>
        <polyline points="222,259 296,132"/>
        <polyline points="443,132 517,259 540,259"/>
        <polyline points="517,259 443,386 443,402"/>
      </g>
    </svg>

    <h1 class="headline">
      <span class="line-main">Honigwerkstatt</span>
      <span class="line-sub">Lindenhain</span>
    </h1>

    <p class="intro">Lorem ipsum dolor sit amet, consetetur</p>
  </main>
</body>
</html>
```